***~~__DOG DESIGN PROJECT__~~***

I would like it to be outgoing and modern. We would love to see designs that use happy, bright and shining/glowing colors. The content needs to be laid out on a clean white background for easy reading. Get creative and let the passion you have for dogs spill into your work!

Requirements
Must have
• Social Media Functionality for all the popular platforms(atleast Facebook, twitter, google+, digg, stumbleupon). Space for atleast one advertisement per page. Toggle box for users to view the most recent or most popular pictures and stories. Make it so that each page has side bar to share content to social media platforms stated above with counters showing how many times users "shared" my content. Add at the bottom a place to subscribe to newsletter. Also need space for a facebook plug in box showing like, number of likes and pics of users, on the home page.
Nice to have
• Unique artistic fonts for the logo font of Velvet Paws. Artistic digital/cartoon logo of a dog as the logo(either Golden Retriever, German Shepherd, or Chihuahua in a circle or orb - if done professionally I will pay additional sum. Look at the color green in the file attachment as a reference for color scheme. And the other attachment is an example of my favorite directory banner - just a guideline of style to aim for. Don't let any of this hinder your creativity.
Should not have
• Do not submit a plain design. It needs to stand out! Also the background of the text needs to be white, so don't send colored backgrounds behind the text. Though a shiny, pearl white would be nice!

```html
<!DOCTYPE html>
<html lang="en">
<head>
<meta charset="utf-8">
<title>Velvet Paws</title>
<link href="https://fonts.googleapis.com/css2?family=Alice&family=Crimson+Text&family=PT+Sans:ital,wght@0,400;0,700;1,400&display=swap" rel="stylesheet">
<style>
:root{
  --lime-light:#c8e87a;
  --lime:#9ccc3a;
  --lime-dark:#7bb21a;
  --green-text:#8dbb1c;
  --sky:#48c3e6;
  --sky-dark:#17a6d2;
  --sky-light:#8adcf3;
  --link:#27b2dc;
  --ink:#2b2b2b;
  --white:#ffffff;
  --panel-grey:#f3f3f3;
}
*{margin:0;padding:0;box-sizing:border-box}
html,body{width:1200px;height:1152px;overflow:hidden}
body{
  position:relative;
  font-family:"PT Sans",sans-serif;
  background:radial-gradient(ellipse at 35% 15%,var(--lime-light) 0%,var(--lime) 55%,var(--lime-dark) 100%);
}
.abs{position:absolute}

/* header */
.nav-ribbon{left:112px;top:108px;width:980px;height:63px}
.nav-link{position:absolute;top:133px;font-style:italic;font-size:15px;color:var(--white);display:flex;align-items:center;gap:6px}
.nav-link::before{content:"";width:8px;height:8px;border-radius:50%;background:var(--white)}
.nav-link.is-active{color:#e6f97a}
.nav-link.is-active::before{background:#e6f97a}
.logo-disc{left:538px;top:-4px;width:124px;height:124px;border-radius:50%;
  background:radial-gradient(circle at 45% 35%,#fff 0%,#eef4f6 60%,#cfdde3 100%);
  box-shadow:0 2px 6px rgba(0,0,0,.2)}
.logo-tab{left:453px;top:101px;width:294px;height:67px;border-radius:6px;
  background:linear-gradient(#6fd3f0,#2fb6e0);border:2px solid #8ee0f6;
  display:flex;align-items:center;justify-content:center}
.logo-name{font-family:"Alice",serif;font-size:42px;color:var(--white)}

/* main panel */
.panel{left:120px;top:182px;width:960px;height:946px;background:var(--white);
  box-shadow:0 0 12px rgba(0,0,0,.15)}
.pager{top:193px;height:16px;font-size:11px;color:var(--white);display:flex;align-items:center;justify-content:center;background:var(--sky-light)}
.pager.prev{left:955px;width:56px}
.pager.next{left:1013px;width:55px;background:var(--sky);color:#064a60}

.slider{left:147px;top:210px;width:566px;height:288px;border:6px solid var(--sky);border-radius:4px;
  background:linear-gradient(180deg,#4f7a1c 0%,#8fb345 30%,#d8c28f 55%,#c9b07a 75%,#6f8e3a 100%);overflow:hidden}
.slider-caption{position:absolute;left:0;right:0;bottom:0;height:48px;background:rgba(60,60,60,.35);
  font-family:"Alice",serif;font-size:40px;color:rgba(255,255,255,.85);text-align:right;padding-right:18px;line-height:46px}
.slider-arrow{width:30px;height:30px;border-radius:50%;background:var(--sky);top:338px}
.slider-arrow svg{display:block}
.slider-shadow{left:180px;top:500px;width:500px;height:14px;border-radius:50%;
  background:radial-gradient(ellipse,rgba(0,0,0,.25),transparent 70%)}

.ad-slot{left:756px;top:217px;width:286px;height:220px;border:4px solid var(--sky);
  background:linear-gradient(135deg,#6a5442 0%,#3b2c22 50%,#8d7560 100%)}

.welcome{left:730px;top:457px;width:364px;height:45px}
.welcome-text{left:776px;top:463px;font-size:22px;font-weight:700;color:var(--white);letter-spacing:.3px}

/* featured */
.card-photo{top:576px;width:200px;height:134px;border:1px solid #d5e8ee;border-radius:4px;
  box-shadow:3px -3px 0 var(--sky),-2px 3px 0 var(--sky)}
.card-title{top:724px;width:200px;text-align:center;color:var(--green-text);font-size:16px;font-weight:700}
.card-sub{top:747px;width:200px;text-align:center;color:var(--ink);font-size:13px}
.card-link{top:771px;width:200px;text-align:center;color:var(--link);font-size:14px;font-weight:700}

/* lower */
.lower{left:120px;top:816px;width:960px;height:255px;background:linear-gradient(#fbfbfb,#f0f0f0)}
.divider{top:842px;width:2px;height:196px;background:linear-gradient(transparent,#e3e3e3,transparent)}
.list-head{top:840px;font-size:21px;font-weight:700;color:var(--green-text)}
.story-list{list-style:none;top:877px;font-size:13px;color:var(--ink)}
.story-list li{height:21px;display:flex;align-items:center;gap:10px}
.story-list li::before{content:"";width:9px;height:9px;border-radius:50%;background:var(--lime)}

.newsletter{left:799px;top:828px;width:265px;height:142px;border-radius:5px;
  background:linear-gradient(#7fd6f1,#3dbbe3);border:2px solid #a8e6f7}
.field{left:809px;width:238px;height:29px;border-radius:6px;background:var(--white);
  font-size:13px;color:#4a8fa6;padding-left:14px;line-height:29px}
.subscribe{left:829px;top:933px;width:209px;height:28px;border-radius:6px;
  background:linear-gradient(#70cfee,#34b3df);border:1px solid #bfeefb;color:var(--white);
  font-size:16px;font-weight:700;text-align:center;line-height:26px;letter-spacing:.3px}
.follow{left:819px;top:976px;font-size:22px;font-weight:700;color:var(--green-text)}
.share-count{top:1005px;width:30px;height:16px;background:#2b2b2b;color:var(--white);font-size:11px;text-align:center;line-height:16px;border-radius:2px}
.share-btn{top:1018px;width:44px;height:44px;border-radius:50%;border:3px solid #e7eef2;box-shadow:0 2px 4px rgba(0,0,0,.25)}

.footer-link{top:1032px;font-family:"Crimson Text",serif;font-size:18px;color:var(--green-text)}

.footer-band{left:103px;top:1071px;width:993px;height:50px;background:linear-gradient(#7fd6f1,#37b6e0);
  box-shadow:0 2px 6px rgba(0,0,0,.2)}
.copyright{left:103px;top:1089px;width:993px;text-align:center;font-size:13px;color:#2c3c44}
</style>
</head>
<body>

<header>
  <svg class="abs nav-ribbon" viewBox="0 0 980 63" aria-hidden="true">
    <defs>
      <linearGradient id="ribbonFill" x1="0" y1="0" x2="0" y2="1">
        <stop offset="0" stop-color="#4cc6ea"/><stop offset="1" stop-color="#15a3d0"/>
      </linearGradient>
    </defs>
    <polygon points="0,0 980,0 962,31 980,63 0,63 18,31" fill="url(#ribbonFill)"/>
  </svg>
  <div class="abs logo-disc" aria-hidden="true"></div>
  <nav>
    <span class="nav-link is-active" style="left:146px">Home</span>
    <span class="nav-link" style="left:214px">Stories</span>
    <span class="nav-link" style="left:296px">Photos</span>
    <span class="nav-link" style="left:370px">Videos</span>
    <span class="nav-link" style="left:768px">Fun</span>
    <span class="nav-link" style="left:837px">Contests</span>
    <span class="nav-link" style="left:920px">Contact Us</span>
  </nav>
  <div class="abs logo-tab"><span class="logo-name">Velvet Paws</span></div>
</header>

<main>
  <div class="abs panel"></div>

  <span class="abs pager prev">Previous</span>
  <span class="abs pager next">Next</span>

  <div class="abs slider-shadow"></div>
  <div class="abs slider" role="img" aria-label="Photo of five yellow labrador puppies lying on grass">
    <div class="slider-caption">Velvet Paws</div>
  </div>
  <div class="abs slider-arrow" style="left:129px"><svg width="30" height="30" viewBox="0 0 30 30"><path d="M17 9 L11 15 L17 21" stroke="#fff" stroke-width="2.5" fill="none"/></svg></div>
  <div class="abs slider-arrow" style="left:702px"><svg width="30" height="30" viewBox="0 0 30 30"><path d="M13 9 L19 15 L13 21" stroke="#fff" stroke-width="2.5" fill="none"/></svg></div>

  <div class="abs ad-slot" role="img" aria-label="Advertisement: anti-fur campaign poster with a man holding a pug"></div>

  <svg class="abs welcome" viewBox="0 0 364 45" aria-hidden="true">
    <defs>
      <linearGradient id="welcomeFill" x1="0" y1="0" x2="0" y2="1">
        <stop offset="0" stop-color="#6ed1f0"/><stop offset="1" stop-color="#2cb2de"/>
      </linearGradient>
    </defs>
    <polygon points="364,0 364,45 0,45 30,22 0,0" fill="url(#welcomeFill)"/>
  </svg>
  <h1 class="abs welcome-text">Welcome to Velvet Paws</h1>

  <section>
    <div class="abs card-photo" style="left:178px;background:linear-gradient(#f4f2ef,#e6dccb)" role="img" aria-label="Photo of a golden retriever puppy"></div>
    <div class="abs card-photo" style="left:391px;background:linear-gradient(#6aa23a,#a8b57a)" role="img" aria-label="Photo of a beagle puppy in a meadow"></div>
    <div class="abs card-photo" style="left:604px;background:linear-gradient(#4a4a4a,#e8e8e8)" role="img" aria-label="Photo of a white puppy behind a crate door"></div>
    <div class="abs card-photo" style="left:818px;background:linear-gradient(#ffffff,#ead8b8)" role="img" aria-label="Photo of a cocker spaniel puppy"></div>

    <div class="abs card-title" style="left:170px">Who is Cute</div>
    <div class="abs card-sub" style="left:170px">Must explain to you</div>
    <div class="abs card-link" style="left:166px">Vote Now</div>

    <div class="abs card-title" style="left:381px">Who is Cute</div>
    <div class="abs card-sub" style="left:380px">Must explain to you</div>
    <div class="abs card-link" style="left:378px">Buy Now</div>

    <div class="abs card-title" style="left:602px">Who is Cute</div>
    <div class="abs card-sub" style="left:602px">Must explain to you</div>
    <div class="abs card-link" style="left:600px">Buy Now</div>

    <div class="abs card-title" style="left:805px">Who is Cute</div>
    <div class="abs card-sub" style="left:805px">Must explain to you</div>
    <div class="abs card-link" style="left:805px">Buy Now</div>
  </section>

  <section>
    <div class="abs lower"></div>
    <div class="abs divider" style="left:441px"></div>
    <div class="abs divider" style="left:779px"></div>

    <h2 class="abs list-head" style="left:158px">Most Pawpular:</h2>
    <ul class="abs story-list" style="left:157px">
      <li>Demoralized by the charms consequat</li>
      <li>Praising pain was born aspernatur</li>
      <li>Exercitation ullamco laboris</li>
      <li>Demoralized by the charms laboris</li>
      <li>Praising pain was born vel eum</li>
      <li>Exercitation ullamco laboris vel eum</li>
    </ul>

    <h2 class="abs list-head" style="left:497px">Most Recent:</h2>
    <ul class="abs story-list" style="left:496px">
      <li>Demoralized by the charms consequat</li>
      <li>Praising pain was born aspernatur</li>
      <li>Exercitation ullamco laboris</li>
      <li>Demoralized by the charms laboris</li>
      <li>Praising pain was born vel eum</li>
      <li>Exercitation ullamco laboris vel eum</li>
    </ul>

    <div class="abs newsletter"></div>
    <div class="abs field" style="top:847px">Name</div>
    <div class="abs field" style="top:886px">Email</div>
    <div class="abs subscribe">Subscribe Newsletter</div>

    <div class="abs follow">Follow us</div>
    <span class="abs share-count" style="left:829px">20</span>
    <span class="abs share-count" style="left:882px">233</span>
    <span class="abs share-count" style="left:937px">12</span>
    <span class="abs share-count" style="left:987px">18</span>
    <span class="abs share-count" style="left:1034px">06</span>
    <span class="abs share-btn" style="left:814px;background:radial-gradient(circle at 40% 35%,#5f86c8,#2c4f98)" aria-label="Share button 1"></span>
    <span class="abs share-btn" style="left:864px;background:radial-gradient(circle at 40% 35%,#8fe0f8,#2ab0e0)" aria-label="Share button 2"></span>
    <span class="abs share-btn" style="left:914px;background:radial-gradient(circle at 40% 35%,#ef6b5a,#b8251a)" aria-label="Share button 3"></span>
    <span class="abs share-btn" style="left:962px;background:radial-gradient(circle at 40% 35%,#5aa8d8,#1b6aa0)" aria-label="Share button 4"></span>
    <span class="abs share-btn" style="left:1013px;background:radial-gradient(circle at 40% 35%,#9ad7ee,#3aa8d8)" aria-label="Share button 5"></span>

    <nav>
      <span class="abs footer-link" style="left:159px">Cute and Funny</span>
      <span class="abs footer-link" style="left:300px">Dogs</span>
      <span class="abs footer-link" style="left:372px">Cats</span>
      <span class="abs footer-link" style="left:438px">All Pets</span>
      <span class="abs footer-link" style="left:525px">News</span>
      <span class="abs footer-link" style="left:594px">Video</span>
      <span class="abs footer-link" style="left:662px">Who's Cutest</span>
    </nav>
  </section>
</main>

<footer>
  <div class="abs footer-band"></div>
  <p class="abs copyright">Copyright © 2012. www.velvetpaws.com</p>
</footer>

</body>
</html>
```